Sophisticated, clean website reflecting my feminine, playful side to sell my abstract art,

I need a website no more than 3 pages to showcase my paintings, a little about me and some contact info. I do abstracts so looking for something a little edgy, yet feminine and current.
Updates

Hi there, These are some artists websites that I Iike: Marlowevint.com (I like how airy it is) rupertalcombe.com gideonparvell.com (I like how it scrolls) I'll need a place for a photo ( a headshot-i do not have it yet so I'll need to be able to upload that later) as well as an area for my bio. Also, it's important that I will be able to upload any new photos and descriptions easily so it should be user friendly. Lastly, I like in a sunny place so would like to have this seem upbeat and playful as that is how i like to paint. thanks-I'm trying to upload my photos now -

Target Market(s)

ppl ages 35-70 who want large scale art for their homes

Industry/Entity Type

art

Coding

Coded - Design and coding required

Number of Pages Required

3 page

Colors

Designer to choose colors to be used in the design.

Requirements
Must have
• photos of my art, a place for my bio, be easy to reach me. tasteful-nothing too "in your face" -my clients are pretty high end and organized. They like clean lines
Nice to have
• sophisticated background, muted tones in the back-similar clean font throughout-no cursive
Should not have
• too many dark areas. Too many blocks of color. Too serious.

```html
<!DOCTYPE html>
<html lang="en">
<head>
<meta charset="utf-8">
<title>Helena Sorvik — Art Gallery</title>
<link href="https://fonts.googleapis.com/css2?family=Playfair+Display:wght@400;500&family=Source+Sans+3:wght@400;600;700&display=swap" rel="stylesheet">
<style>
:root{
  --ink:#111111;
  --white:#ffffff;
  --soft:#f2f2f2;
  --footer:#222222;
  --muted:#555555;
  --star:#f2c200;
  --sage:#9aa08a;
  --line:#cfcfcf;
}
*{margin:0;padding:0;box-sizing:border-box}
html,body{width:1200px;height:4669px;overflow:hidden;background:var(--white)}
body{position:relative;font-family:"Source Sans 3",sans-serif;color:var(--ink)}
.abs{position:absolute}
.serif{font-family:"Playfair Display",serif;font-weight:400}
.icon-circle{position:absolute;width:32px;height:32px;border:1.5px solid var(--ink);border-radius:50%;display:flex;align-items:center;justify-content:center}
.icon-circle svg{width:15px;height:15px}
.site-name{left:0;width:1200px;top:22px;text-align:center;font-size:31px;font-weight:500}
.login-btn{left:974px;top:16px;width:125px;height:49px;border:1.5px solid #999;display:flex;align-items:center;justify-content:center;font-weight:700;font-size:15px}
.main-nav{left:0;width:1200px;top:84px;display:flex;justify-content:center;gap:26px;font-size:10px;font-weight:600}
.main-nav .current{text-decoration:underline}
.hero{left:0;top:130px;width:1200px;height:501px;background:linear-gradient(120deg,#6a4a30 0%,#7a5a3a 8%,#2f9c84 14%,#e6ebe4 30%,#5aa84a 48%,#8cc45a 62%,#3f9a56 80%,#6cb050 100%)}
.hero-title{left:0;width:1200px;top:275px;text-align:center;color:var(--white);font-size:50px;font-weight:500}
.btn{position:absolute;display:flex;align-items:center;justify-content:center;font-size:14px;font-weight:700}
.btn-light{background:var(--white);color:var(--ink)}
.btn-dark{background:var(--ink);color:var(--white)}
.dots{left:572px;top:592px;display:flex;gap:7px}
.dots span{width:12px;height:12px;border-radius:50%;background:#777}
.dots span.on{background:#111}
.section-title{left:0;width:1200px;text-align:center;font-size:35px}
.card-img{position:absolute;top:832px;height:268px}
.stars{position:absolute;display:flex;gap:2px;color:var(--star);font-size:17px}
.stars .off{color:#ccc}
.price{position:absolute;width:310px;text-align:center;top:1152px;font-size:21px;font-weight:600}
.card-name{position:absolute;width:310px;text-align:center;top:1193px;font-size:21px;font-weight:600}
.sq{position:absolute;top:1240px;width:49px;height:49px;border:1.5px solid var(--ink);display:flex;align-items:center;justify-content:center}
.sq svg{width:24px;height:24px}
.about-photo{left:0;top:1383px;width:593px;height:604px;background:linear-gradient(160deg,#4a4a4a,#3a3a3a 60%,#d9d9d9 90%)}
.about-panel{left:593px;top:1383px;width:607px;height:604px;background:var(--soft)}
.about-title{left:662px;top:1470px;font-size:33px}
.about-text{left:662px;top:1577px;width:437px;font-size:13.2px;line-height:22.5px;color:#333}
.name-mark{font-family:"Source Sans 3",sans-serif;font-weight:700;font-size:40px;line-height:1.05}
.quote-box{left:437px;top:2208px;width:662px;height:203px;border:1.5px solid #999;background:var(--white)}
.quote-shadow{left:437px;top:2208px;width:662px;height:203px;border-left:5px solid var(--ink);border-bottom:5px solid var(--ink)}
.quote-text{left:475px;top:2236px;width:590px;font-size:13.5px;line-height:22.5px;color:#333}
.arrow-dot{position:absolute;width:27px;height:27px;border-radius:50%;display:flex;align-items:center;justify-content:center}
.avatar{left:593px;top:2485px;width:62px;height:62px;border-radius:50%;background:linear-gradient(#b9a48e,#7d7466)}
.reviewer{left:675px;top:2493px;font-size:13px;font-weight:700}
.reviewer-role{left:675px;top:2516px;font-size:13px;color:#333}
.gallery-bg{left:0;top:2660px;width:1200px;height:971px;background:var(--soft)}
.tile{position:absolute}
.footer{left:0;top:4246px;width:1200px;height:423px;background:var(--footer);color:var(--white)}
.foot-title{position:absolute;font-family:"Playfair Display",serif;font-size:22px}
.foot-link{position:absolute;font-size:13px}
.foot-contact{position:absolute;font-size:13px;display:flex;align-items:center;gap:14px}
.foot-contact .icon-circle{position:static;border-color:var(--white);width:30px;height:30px}
.email-field{left:821px;top:4404px;width:196px;height:61px;background:var(--white);color:#666;font-size:11px;padding:24px 26px}
.email-send{left:1017px;top:4404px;width:82px;height:61px;background:var(--sage);display:flex;align-items:center;justify-content:center}
.legal{position:absolute;top:4626px;font-size:10px}
</style>
</head>
<body>

<!-- Header -->
<header>
  <div class="icon-circle" style="left:100px;top:25px" aria-label="Social profile one"></div>
  <div class="icon-circle" style="left:144px;top:25px" aria-label="Social profile two"></div>
  <div class="icon-circle" style="left:188px;top:25px" aria-label="Social profile three"></div>
  <div class="icon-circle" style="left:232px;top:25px" aria-label="Email">
    <svg viewBox="0 0 16 16" fill="none" stroke="#111" stroke-width="1.4"><rect x="2" y="3.5" width="12" height="9" rx="1"/><path d="M2.5 4.5 8 9l5.5-4.5"/></svg>
  </div>
  <div class="icon-circle" style="left:276px;top:25px" aria-label="Phone">
    <svg viewBox="0 0 16 16" fill="none" stroke="#111" stroke-width="1.4"><path d="M4 2.5h2.5l1 3-1.5 1a7 7 0 0 0 3.5 3.5l1-1.5 3 1V12a1.5 1.5 0 0 1-1.5 1.5A10 10 0 0 1 2.5 4 1.5 1.5 0 0 1 4 2.5z"/></svg>
  </div>
  <div class="abs serif site-name">Helena Sorvik</div>
  <div class="icon-circle" style="left:823px;top:25px" aria-label="Account">
    <svg viewBox="0 0 16 16" fill="#111"><circle cx="8" cy="5.5" r="2.8"/><path d="M2.8 13.5c.6-3 2.6-4.3 5.2-4.3s4.6 1.3 5.2 4.3z"/></svg>
  </div>
  <div class="icon-circle" style="left:867px;top:25px" aria-label="Wishlist">
    <svg viewBox="0 0 16 16" fill="none" stroke="#111" stroke-width="1.4"><path d="M8 13.5 2.7 8.3a3 3 0 0 1 4.3-4.3L8 5l1-1a3 3 0 0 1 4.3 4.3z"/></svg>
  </div>
  <div class="icon-circle" style="left:911px;top:25px" aria-label="Cart">
    <svg viewBox="0 0 16 16" fill="none" stroke="#111" stroke-width="1.4"><path d="M1.5 2.5h2l1.8 7.5h7l1.5-5.5H4.2"/><circle cx="6" cy="12.8" r="1"/><circle cx="11.5" cy="12.8" r="1"/></svg>
  </div>
  <div class="abs login-btn">Login</div>
  <nav class="abs main-nav">
    <span class="current">Home</span><span>Featured Collection</span><span>Reviews</span><span>Art Gallery</span><span>About The Artist</span>
  </nav>
</header>

<!-- Hero -->
<section>
  <div class="abs hero" role="img" aria-label="Close-up of a green and teal abstract painting on a wooden easel"></div>
  <h1 class="abs serif hero-title">Welcome To My Art Gallery</h1>
  <div class="btn btn-light" style="left:506px;top:370px;width:187px;height:49px">Explore All</div>
  <div class="abs dots"><span></span><span class="on"></span><span></span></div>
</section>

<!-- Featured Collection -->
<section>
  <h2 class="abs serif section-title" style="top:724px">Featured Collection</h2>

  <div class="card-img" style="left:100px;width:310px;background:linear-gradient(135deg,#2f6e6a,#c7661f 35%,#e8e4da 55%,#253f3d 80%,#8a3a18)" role="img" aria-label="Orange, teal and white abstract painting"></div>
  <div class="card-img" style="left:446px;width:308px;background:linear-gradient(90deg,#0f7f78 0%,#0f7f78 12%,#d8d4c8 18%,#cfcab9 45%,#1f2f66 60%,#23356f 100%)" role="img" aria-label="Teal, cream and navy abstract painting"></div>
  <div class="card-img" style="left:792px;width:308px;background:linear-gradient(90deg,#7b88a8 0%,#8592b0 22%,#e4ddc9 30%,#0f8070 40%,#0f8070 68%,#e4ddc9 75%,#22326c 88%,#22326c 100%)" role="img" aria-label="Blue, green and cream striped abstract painting"></div>

  <div class="stars" style="left:207px;top:1118px">★★★★<span class="off">★</span></div>
  <div class="stars" style="left:552px;top:1118px">★★★★<span class="off">★</span></div>
  <div class="stars" style="left:898px;top:1118px">★★★★★</div>

  <div class="price" style="left:100px">$50.00</div>
  <div class="price" style="left:446px">$68.00</div>
  <div class="price" style="left:792px">$75.90</div>

  <div class="card-name" style="left:100px">Coloured Painting</div>
  <div class="card-name" style="left:446px">Coloured Painting</div>
  <div class="card-name" style="left:792px">Coloured Painting</div>

  <div class="btn btn-dark" style="left:103px;top:1240px;width:176px;height:49px;font-size:13px">Buy Now</div>
  <div class="sq" style="left:292px"><svg viewBox="0 0 24 24" fill="none" stroke="#111" stroke-width="1.6"><path d="M12 20 4 12.2a4.5 4.5 0 0 1 6.4-6.4L12 7.4l1.6-1.6a4.5 4.5 0 0 1 6.4 6.4z"/></svg></div>
  <div class="sq" style="left:353px"><svg viewBox="0 0 24 24" fill="none" stroke="#111" stroke-width="1.6"><path d="M2.5 4h3l2.6 11h10.4L20.8 7H6.5"/><circle cx="9" cy="19" r="1.4"/><circle cx="17" cy="19" r="1.4"/><path d="M13 8.5v4M11 10.5h4"/></svg></div>

  <div class="btn btn-dark" style="left:449px;top:1240px;width:176px;height:49px;font-size:13px">Buy Now</div>
  <div class="sq" style="left:638px"><svg viewBox="0 0 24 24" fill="none" stroke="#111" stroke-width="1.6"><path d="M12 20 4 12.2a4.5 4.5 0 0 1 6.4-6.4L12 7.4l1.6-1.6a4.5 4.5 0 0 1 6.4 6.4z"/></svg></div>
  <div class="sq" style="left:699px"><svg viewBox="0 0 24 24" fill="none" stroke="#111" stroke-width="1.6"><path d="M2.5 4h3l2.6 11h10.4L20.8 7H6.5"/><circle cx="9" cy="19" r="1.4"/><circle cx="17" cy="19" r="1.4"/><path d="M13 8.5v4M11 10.5h4"/></svg></div>

  <div class="btn btn-dark" style="left:795px;top:1240px;width:176px;height:49px;font-size:13px">Buy Now</div>
  <div class="sq" style="left:983px"><svg viewBox="0 0 24 24" fill="none" stroke="#111" stroke-width="1.6"><path d="M12 20 4 12.2a4.5 4.5 0 0 1 6.4-6.4L12 7.4l1.6-1.6a4.5 4.5 0 0 1 6.4 6.4z"/></svg></div>
  <div class="sq" style="left:1045px"><svg viewBox="0 0 24 24" fill="none" stroke="#111" stroke-width="1.6"><path d="M2.5 4h3l2.6 11h10.4L20.8 7H6.5"/><circle cx="9" cy="19" r="1.4"/><circle cx="17" cy="19" r="1.4"/><path d="M13 8.5v4M11 10.5h4"/></svg></div>
</section>

<!-- About -->
<section>
  <div class="abs about-photo" role="img" aria-label="Portrait of the artist in a white off-shoulder blouse against a dark grey backdrop"></div>
  <div class="abs about-panel"></div>
  <h2 class="abs serif about-title">About The Artist</h2>
  <p class="abs about-text">Lorem ipsum dolor sit amet, consectetur adipiscing elit. Consequat quis turpis adipiscing tincidunt. Fames ut lectus tempus quis lacus nunc arcu. Mi, ultrices varius ultrices massa aliquam odio enim quam. Quisque libero sed eget pellentesque imperdiet. At et lorem habitant amet morbi velit, sed eu lorem. Egestas egestas mattis ultrices aliquam. Malesuada at malesuada convallis feugiat. Pharetra venenatis odio duis quis semper amet. Amet justo, enim ac lacus, aenean elementum. Commodo fermentum viverra consectetur at elit mauris a orci. Quis molestie cursus nisi lorem mi.<br>Suscipit cursus sagittis odio ut sit in aliquam at amet. Leo orci sed mauris sit morbi mi diam vestibulum. Ultrices aliquam donec semper gravida nibh dictum dui. Suspendisse ultrices egestas dui a, faucibus. Eget a id placerat semper consectetur. Integer augue tortor etiam quis. Euismod imperdiet elit proin fames felis lectus justo.</p>
</section>

<!-- Reviews -->
<section>
  <h2 class="abs serif section-title" style="top:2080px;left:-26px">Reviews</h2>
  <div class="abs name-mark" style="left:103px;top:2320px;width:230px">Helena<br>Sorvik</div>

  <div class="abs quote-shadow"></div>
  <div class="abs quote-box" style="left:441px;top:2208px;width:658px;height:198px"></div>
  <svg class="abs" style="left:580px;top:2400px" width="100" height="62" viewBox="0 0 100 62">
    <path d="M2 6 L2 60 L95 6" fill="#fff" stroke="none"/>
    <path d="M2 6 L2 60 L95 6" fill="none" stroke="#111" stroke-width="4"/>
    <path d="M4 6 H96" stroke="#fff" stroke-width="6"/>
  </svg>
  <p class="abs quote-text">Lorem ipsum dolor sit amet, consectetur adipiscing elit. Ac est eget integer odio adipiscing a justo. Tortor in pellentesque at consectetur tempus. Pharetra quisque orci, nunc, gravida imperdiet. Lobortis ullamcorper augue lectus dui amet congue tempus, pharetra nibh. Gravida auctor id dignissim scelerisque velit aliquam dignissim eleifend. Phasellus nunc nisi, euismod arcu vitae at ut massa id. Viverra vitae at fringilla proin lectus sapien libero, diam. Sapien porttitor ac feugiat donec non velit augue sem. Amet elit eget porttitor vitae ut elit.</p>
  <div class="arrow-dot" style="left:426px;top:2289px;background:#111">
    <svg width="12" height="12" viewBox="0 0 12 12" fill="#fff"><path d="M8 2 3 6l5 4z"/></svg>
  </div>
  <div class="arrow-dot" style="left:1086px;top:2289px;background:var(--sage)">
    <svg width="12" height="12" viewBox="0 0 12 12" fill="#fff"><path d="M4 2l5 4-5 4z"/></svg>
  </div>
  <div class="abs avatar" role="img" aria-label="Reviewer portrait"></div>
  <div class="abs reviewer">CORIN ALDER</div>
  <div class="abs reviewer-role">Lorem ipsum dolor</div>
  <div class="stars" style="left:850px;top:2502px;font-size:19px">★★★★★</div>
</section>

<!-- Art Gallery -->
<section>
  <div class="abs gallery-bg"></div>
  <h2 class="abs serif section-title" style="top:2752px">Art Gallery</h2>
  <div class="tile" style="left:102px;top:2861px;width:320px;height:272px;background:linear-gradient(90deg,#0f7f78 0%,#0f7f78 10%,#d8d4c8 18%,#c9c5b6 48%,#23356f 62%,#2a3d78 100%)" role="img" aria-label="Teal, cream and navy abstract painting"></div>
  <div class="tile" style="left:440px;top:2861px;width:321px;height:272px;background:linear-gradient(135deg,#e9e6dc 0%,#d9b84a 30%,#e6e2d6 55%,#2c4f8c 72%,#b07a45 90%)" role="img" aria-label="Cream canvas with yellow and blue floral swirls on wood"></div>
  <div class="tile" style="left:778px;top:2861px;width:321px;height:272px;background:linear-gradient(180deg,#c8a27a 0%,#e3ddd0 18%,#3a82b6 45%,#d8dbe0 80%,#e0d8c8 100%)" role="img" aria-label="Blue paint drips on a pale canvas over wood"></div>
  <div class="tile" style="left:102px;top:3165px;width:320px;height:272px;background:linear-gradient(135deg,#d7a02a 0%,#f0e2b0 35%,#c67a1a 55%,#2e4d7a 75%,#e2b84a 100%)" role="img" aria-label="Golden yellow and navy abstract swirl painting"></div>
  <div class="tile" style="left:440px;top:3165px;width:321px;height:272px;background:linear-gradient(135deg,#7fbf5a 0%,#2f8a4c 35%,#e6ecde 50%,#5fae46 70%,#b08a5a 100%)" role="img" aria-label="Green abstract painting on wood"></div>
  <div class="tile" style="left:778px;top:3165px;width:321px;height:272px;background:linear-gradient(135deg,#e8e2da 0%,#6a2a1e 35%,#9a4a36 55%,#e6ddd4 80%,#b59b84 100%)" role="img" aria-label="Deep burgundy brushwork on a white canvas"></div>
  <div class="btn btn-dark" style="left:506px;top:3488px;width:188px;height:49px">View All</div>
</section>

<!-- Instagram -->
<section>
  <h2 class="abs serif section-title" style="top:3724px">Follow Me On Instagram</h2>
  <div class="tile" style="left:103px;top:3833px;width:240px;height:206px;background:linear-gradient(135deg,#e6e2ea,#7a5aa8 45%,#cbbcd8 70%,#4a3a7a)" role="img" aria-label="Purple and lilac abstract painting"></div>
  <div class="tile" style="left:355px;top:3833px;width:240px;height:206px;background:linear-gradient(135deg,#e8ddd4,#a8321e 45%,#e2cbbb 75%,#b07a50)" role="img" aria-label="Red swirl abstract painting"></div>
  <div class="tile" style="left:607px;top:3833px;width:240px;height:206px;background:linear-gradient(135deg,#c99aa0,#6a3a4a 40%,#e8b8a8 65%,#d58a7a)" role="img" aria-label="Pink and plum floral abstract painting"></div>
  <div class="tile" style="left:859px;top:3833px;width:240px;height:206px;background:linear-gradient(135deg,#e6c8c2,#8a3a4a 45%,#e8b4b0 70%,#c77a80)" role="img" aria-label="Rose pink floral abstract painting"></div>
  <div class="btn btn-dark" style="left:506px;top:4103px;width:188px;height:49px">Follow</div>
</section>

<!-- Footer -->
<footer class="abs footer">
  <div class="abs name-mark" style="left:100px;top:92px;width:200px;color:var(--white)">Helena<br>Sorvik</div>

  <div class="foot-title" style="left:384px;top:97px">Quick Links</div>
  <div class="foot-link" style="left:384px;top:159px">Home</div>
  <div class="foot-link" style="left:384px;top:190px">Featured Collection</div>
  <div class="foot-link" style="left:384px;top:221px">Reviews</div>
  <div class="foot-link" style="left:384px;top:252px">Art Gallery</div>
  <div class="foot-link" style="left:384px;top:283px">About The Artist</div>

  <div class="foot-title" style="left:557px;top:97px">Contact Info</div>
  <div class="foot-contact" style="left:557px;top:156px">
    <div class="icon-circle"><svg viewBox="0 0 16 16" fill="none" stroke="#fff" stroke-width="1.4"><path d="M4 2.5h2.5l1 3-1.5 1a7 7 0 0 0 3.5 3.5l1-1.5 3 1V12a1.5 1.5 0 0 1-1.5 1.5A10 10 0 0 1 2.5 4 1.5 1.5 0 0 1 4 2.5z"/></svg></div>
    <span>000.000.0000</span>
  </div>
  <div class="foot-contact" style="left:557px;top:199px">
    <div class="icon-circle"><svg viewBox="0 0 16 16" fill="#fff"><path d="M8 1.5a4.5 4.5 0 0 0-4.5 4.5C3.5 9.5 8 14.5 8 14.5s4.5-5 4.5-8.5A4.5 4.5 0 0 0 8 1.5zm0 6.2a1.7 1.7 0 1 1 0-3.4 1.7 1.7 0 0 1 0 3.4z"/></svg></div>
    <span>14 Solana Lane, Studio 3</span>
  </div>
  <div class="foot-contact" style="left:557px;top:242px">
    <div class="icon-circle"><svg viewBox="0 0 16 16" fill="none" stroke="#fff" stroke-width="1.4"><rect x="2" y="3.5" width="12" height="9" rx="1"/><path d="M2.5 4.5 8 9l5.5-4.5"/></svg></div>
    <span>studio@helenasorvik.art</span>
  </div>

  <div class="foot-title" style="left:821px;top:97px">Newsletter</div>
  <div class="abs email-field" style="top:158px">Email</div>
  <div class="abs email-send" style="top:158px">
    <svg width="24" height="24" viewBox="0 0 24 24" fill="none" stroke="#fff" stroke-width="1.6"><path d="M21 3 3 10.5l7 2.5 2.5 7z"/><path d="M21 3 10 13"/></svg>
  </div>
  <div class="icon-circle" style="left:821px;top:251px;border-color:var(--white)" aria-label="Social profile one"></div>
  <div class="icon-circle" style="left:865px;top:251px;border-color:var(--white)" aria-label="Social profile two"></div>
  <div class="icon-circle" style="left:909px;top:251px;border-color:var(--white)" aria-label="Social profile three"></div>

  <div class="legal" style="left:102px;top:380px">Terms Of Use</div>
  <div class="legal" style="left:196px;top:380px">Privacy Policy</div>
  <div class="legal" style="right:101px;top:380px">© 2022 Art Gallery. ALL RIGHTS RESERVED</div>
</footer>

</body>
</html>
```